Brightwave Business Card

Professional Business Card Design required using the attached contact information.

Contact information can be rearranged as required.

The company is a new start up venture developing solar systems, the branding should be in keeping with that of one of the investors whose website is as follows https://www.quorvex.com/

```html
<!DOCTYPE html>
<html lang="en">
<head>
<meta charset="utf-8">
<title>Brightwave Renewables – Business Card</title>
<link rel="stylesheet" href="https://fonts.googleapis.com/css2?family=Dosis:wght@400;500;600&family=Montserrat:wght@600&display=swap">
<style>
  :root {
    --backdrop: #1f2a3d;
    --brand-green: #237a3b;
    --card-white: #ffffff;
    --ink-slate: #4c5d6e;
    --ink-muted: #5d6e7e;
  }
  * { margin: 0; padding: 0; box-sizing: border-box; }
  html, body { width: 1000px; height: 1200px; overflow: hidden; }
  body { background: var(--backdrop); position: relative; }

  .card {
    position: absolute;
    left: 178px;
    width: 645px;
    height: 430px;
  }
  .card-front { top: 145px; background: var(--brand-green); }
  .card-back  { top: 625px; background: var(--card-white); font-family: "Dosis", sans-serif; }

  .front-wordmark {
    position: absolute;
    left: 0; right: 0;
    top: 212px;
    text-align: center;
    font-family: "Montserrat", sans-serif;
    font-weight: 600;
    font-size: 29px;
    letter-spacing: 0.5px;
    color: var(--card-white);
  }

  .company-name {
    position: absolute;
    left: 55px;
    top: 72px;
    font-weight: 500;
    font-size: 31px;
    line-height: 31px;
    color: var(--brand-green);
  }

  .person {
    position: absolute;
    left: 55px;
    top: 275px;
  }
  .person-name {
    font-weight: 600;
    font-size: 29px;
    line-height: 27px;
    color: var(--brand-green);
  }
  .person-title {
    margin-top: 4px;
    font-weight: 400;
    font-size: 19px;
    color: var(--ink-muted);
  }

  .contact-list {
    position: absolute;
    left: 228px;
    top: 272px;
    list-style: none;
  }
  .contact-item {
    display: flex;
    align-items: center;
    height: 29.5px;
    font-weight: 500;
    font-size: 20px;
    color: var(--ink-slate);
  }
  .contact-icon {
    width: 20px;
    height: 20px;
    margin-right: 14px;
    fill: var(--ink-slate);
    flex: none;
  }
</style>
</head>
<body>
  <section class="card card-front" aria-label="Card front">
    <p class="front-wordmark">BRIGHTWAVE RENEWABLES</p>
  </section>

  <section class="card card-back" aria-label="Card back">
    <h1 class="company-name">BRIGHTWAVE<br>RENEWABLES LLC</h1>

    <div class="person">
      <p class="person-name">DANIEL<br>HARTWELL</p>
      <p class="person-title">Founder/CEO</p>
    </div>

    <ul class="contact-list">
      <li class="contact-item">
        <svg class="contact-icon" viewBox="0 0 24 24" aria-hidden="true"><path d="M6.6 10.8a15.1 15.1 0 0 0 6.6 6.6l2.2-2.2a1 1 0 0 1 1-.25 11.4 11.4 0 0 0 3.6.57 1 1 0 0 1 1 1V20a1 1 0 0 1-1 1A17 17 0 0 1 3 4a1 1 0 0 1 1-1h3.5a1 1 0 0 1 1 1c0 1.25.2 2.45.57 3.57a1 1 0 0 1-.25 1z"/></svg>
        +1 (555) 240-7713
      </li>
      <li class="contact-item">
        <svg class="contact-icon" viewBox="0 0 24 24" aria-hidden="true"><path d="M3 5h18v14H3z" opacity="0.9"/><path d="M3 5l9 7 9-7" fill="none" stroke="#fff" stroke-width="1.6"/></svg>
        daniel.hartwell@brightwave-renewables.com
      </li>
      <li class="contact-item">
        <svg class="contact-icon" viewBox="0 0 24 24" aria-hidden="true"><path d="M12 2a7 7 0 0 0-7 7c0 5.2 7 13 7 13s7-7.8 7-13a7 7 0 0 0-7-7zm0 9.5A2.5 2.5 0 1 1 12 6.5a2.5 2.5 0 0 1 0 5z"/></svg>
        210 Harbor Street, Boston, MA 02110
      </li>
    </ul>
  </section>
</body>
</html>
```